Carpentry and Building Business Card

I'm looking for a business card that is minimalistic and that incorporates the theme of my Velmi logo.
On one side I'd like the VELMI logo with my details on the other side.
Double sided with curved edges

Target Market(s)

Construction / renovation
Adults

Industry/Entity Type

Tradesman

Contact Information for Business Card

Logo on one side, details on the other

Colors

Designer to choose only greyscale colors for use in the design.

Requirements
Must have
• Niko Barlettis
VELMI CONSTRUCT
Carpentry & Building Services
0412385726
Velmiconstruct@brindlemail.com
Lic No. 618243D
Nice to have
• Fb and insta icons. @velmiconstruct
Should not have
• No hammer or tool icons please.

No address line.

```html
<!DOCTYPE html>
<html lang="en">
<head>
<meta charset="utf-8">
<title>Velmi Construct – Business Card</title>
<link rel="stylesheet" href="https://fonts.googleapis.com/css2?family=Montserrat:wght@300;400;600;700&family=Poppins:wght@300;400&display=swap">
<style>
  :root {
    --backdrop: #d6d6d6;
    --card-white: #ffffff;
    --card-black: #0b0b0b;
    --ink: #1e1e1e;
    --ink-soft: #3a3a3a;
    --accent: #ec9a3c;
    --paper-light: #f4f4f4;
  }
  * { box-sizing: border-box; margin: 0; padding: 0; }
  html, body {
    width: 1200px; height: 800px; overflow: hidden;
    background: var(--backdrop);
  }
  .canvas {
    position: relative; width: 1200px; height: 800px;
    display: flex; align-items: center; justify-content: center; gap: 60px;
  }
  .card {
    position: relative; width: 500px; height: 286px;
    border-radius: 12px; overflow: hidden;
    box-shadow: 0 10px 28px rgba(0,0,0,0.18);
  }

  /* Details side */
  .card--details { background: var(--card-white); color: var(--ink); }
  .brand-block { position: absolute; left: 34px; top: 26px; }
  .brand-name {
    font-family: "Montserrat", sans-serif; font-weight: 600;
    font-size: 34px; letter-spacing: 12px; line-height: 1;
  }
  .brand-sub {
    font-family: "Montserrat", sans-serif; font-weight: 300;
    font-size: 30px; letter-spacing: 3px; line-height: 1.05;
  }
  .brand-services {
    font-family: "Montserrat", sans-serif; font-weight: 400;
    font-size: 8.5px; letter-spacing: 1.4px; margin-top: 3px;
  }
  .rule {
    width: 12px; height: 2px; background: var(--ink); margin: 14px 0 7px;
  }
  .person {
    font-family: "Montserrat", sans-serif; font-size: 14px; letter-spacing: 0.5px;
  }
  .person__first { font-weight: 700; }
  .person__last { font-weight: 300; }

  .contacts {
    position: absolute; left: 34px; top: 168px;
    font-family: "Poppins", sans-serif; font-weight: 300; font-size: 11px;
    list-style: none; color: var(--ink-soft);
  }
  .contacts li { display: flex; align-items: center; gap: 6px; height: 17px; }
  .icon {
    width: 12px; height: 12px; border: 1.2px solid var(--accent);
    border-radius: 2px; display: inline-flex; align-items: center; justify-content: center;
  }
  .icon svg { width: 8px; height: 8px; }
  .icon--plain { }
  .licence {
    margin-top: 6px; font-family: "Poppins", sans-serif; font-weight: 300;
    font-size: 11px; color: var(--ink-soft);
  }
  .accent-frame {
    position: absolute; right: -60px; bottom: -70px;
    width: 230px; height: 230px;
    border: 5px solid var(--accent);
  }

  /* Logo side */
  .card--logo {
    background: linear-gradient(135deg, #151515, var(--card-black));
    display: flex; align-items: center; justify-content: center; gap: 12px;
  }
  .logo-mark {
    width: 22px; height: 22px; border: 2px solid var(--accent);
  }
  .logo-name {
    font-family: "Montserrat", sans-serif; font-weight: 400;
    font-size: 26px; letter-spacing: 9px; color: var(--paper-light);
  }
</style>
</head>
<body>
<main class="canvas">

  <section class="card card--details" aria-label="Business card, details side">
    <div class="brand-block">
      <div class="brand-name">VELMI</div>
      <div class="brand-sub">CONSTRUCT</div>
      <div class="brand-services">CARPENTRY &amp; BUILDING SERVICES</div>
      <div class="rule"></div>
      <div class="person"><span class="person__first">NIKO</span> <span class="person__last">BARLETTIS</span></div>
    </div>

    <ul class="contacts">
      <li>
        <span class="icon">
          <svg viewBox="0 0 10 10"><path d="M2 1 L4 1 L4.5 3 L3.4 3.8 Q4.5 6 6.2 6.6 L7 5.5 L9 6 L9 8 Q5 9 2.5 5.5 Q1 3 2 1Z" fill="#ec9a3c"/></svg>
        </span>
        0412385726
      </li>
      <li>
        <span class="icon">
          <svg viewBox="0 0 10 10"><rect x="1" y="2" width="8" height="6" fill="none" stroke="#ec9a3c" stroke-width="1"/><path d="M1 2 L5 5.5 L9 2" fill="none" stroke="#ec9a3c" stroke-width="1"/></svg>
        </span>
        Velmiconstruct@brindlemail.com
      </li>
      <li>
        <span class="icon icon--plain"></span>
        <span class="icon icon--plain"></span>
        @velmiconstruct
      </li>
      <li class="licence">Lic No. 618243D</li>
    </ul>

    <div class="accent-frame" aria-hidden="true"></div>
  </section>

  <section class="card card--logo" aria-label="Business card, logo side">
    <span class="logo-mark" aria-hidden="true"></span>
    <span class="logo-name">VELMI.</span>
  </section>

</main>
</body>
</html>
```